Tarnvale Tech Company Website B2B Dev Teams Orbinex

We need a completely new website for this tech company. We offer software as a service to companies that have private Orbinex software. Our clients are developers, tech teams, and companies (B2B). We offer a way to keep Orbinex devices updated worldwide without needing a Mirro Shelf account, which suits corporate-owned single-use devices very well.
Our public is technicians (software developers), not people who use smartphones. Most clients run Tarnvale on tablets, drones, point-of-sale devices, etc.
The most used feature is the background update, which requires no user interaction. Our product helps developers keep their private enterprise applications updated. Some references of what developers like to see:
dovel.com, trandex.com, lunocrest.com, bravik.io, quorel.io
The green doesn't suit it very well. Feel free to change the logo's color (source images .ai .psd attached). The current website has only five small pages. The new one can have five at most (it can have less). The images of the "update strategies" aren't good. It can be replaced by "mock-like" images mimicking how Orbinex interacts with the user. The proportion of the tool icons isn't good. The login and signup forms can be improved a lot.
We hope for a modern website for a tech company with new colors that, at first glance, convey a sense of quality. We want the current standard for SaaS (software as a service) providers' websites.
https://www.tarnvale.com/
NO WORDPRESS.
We want it built using Next, Nuxt, or another good static build tool.

Target Market(s)
Orbinex Software Development
Industry/Entity Type
Software
Coding
Coded - Design and coding required
Number of Pages Required
4 page
Requirements
Must have
- We want it built using Next, Nuxt, or another good static build tool

Nice to have
- Orbinex message notification mockups instead screenshots

Should not have
- wordpress

```html
<!DOCTYPE html>
<html lang="en">
<head>
<meta charset="utf-8">
<title>Tarnvale — Orbinex Enterprise App Management</title>
<link rel="stylesheet" href="https://fonts.googleapis.com/css2?family=Ubuntu:wght@400;500;700&display=swap">
<style>
  :root{
    --orange:#f28a1e;
    --ink:#1f1f1f;
    --muted:#555;
    --cream:#f4ede6;
    --grey:#f0f0f0;
    --dark:#2b2b2b;
    --white:#ffffff;
    --line:#dddddd;
  }
  *{box-sizing:border-box;margin:0;padding:0}
  html,body{width:1200px;height:2708px;overflow:hidden}
  body{position:relative;font-family:"Ubuntu",sans-serif;color:var(--ink);background:var(--white)}
  .abs{position:absolute}

  .hero-band{left:0;top:0;width:1200px;height:580px;background:var(--cream)}
  .brand{font-weight:700;color:var(--orange);font-size:40px;letter-spacing:-1px}
  .site-header .brand{left:104px;top:22px}
  .main-nav{left:520px;top:38px;display:flex;gap:26px;font-size:17px}
  .main-nav a{color:var(--ink);text-decoration:none}
  .main-nav a.active{color:var(--orange);border-bottom:2px solid var(--orange);padding-bottom:3px}
  .btn{display:inline-block;background:var(--orange);color:var(--white);font-weight:700;font-size:16px;border-radius:4px;text-decoration:none;text-align:center;letter-spacing:.5px}
  .btn-signin{left:1000px;top:26px;width:96px;height:44px;line-height:44px}

  .hero-title{left:0;top:168px;width:1200px;text-align:center;font-weight:700;font-size:44px;line-height:52px;text-transform:uppercase}
  .hero-title em{font-style:normal;color:var(--orange)}
  .hero-sub{left:0;top:278px;width:1200px;text-align:center;font-size:17px;color:var(--muted)}
  .btn-hero{left:524px;top:320px;width:152px;height:46px;line-height:46px}
  .hero-photo{left:200px;top:400px;width:800px;height:432px;border-radius:10px;background:linear-gradient(135deg,#b47a52 0%,#6f4a33 40%,#2f3a2c 75%,#8aa07a 100%)}

  .section-title{left:0;width:1200px;text-align:center;font-weight:700;font-size:34px;text-transform:uppercase}
  .section-title em{font-style:normal;color:var(--orange)}

  .step{width:260px}
  .step-num{width:68px;height:68px;background:var(--orange);color:var(--white);font-weight:700;font-size:30px;line-height:68px;text-align:center}
  .step-name{margin-top:26px;color:var(--orange);font-weight:700;font-size:26px}
  .step-detail{margin-top:6px;font-size:17px}

  .strategies-band{left:0;top:1240px;width:1200px;height:620px;background:var(--grey)}
  .strategy{width:232px;text-align:center}
  .strategy-shot{height:272px;border-radius:8px;position:relative;overflow:hidden}
  .strategy-shot .notice{position:absolute;left:62px;width:108px;background:var(--white);border-radius:6px;box-shadow:0 2px 6px rgba(0,0,0,.25)}
  .strategy-name{margin-top:32px;font-weight:500;font-size:22px}

  .tool{width:180px;height:72px;border:2px solid var(--line);border-radius:8px;background:var(--white);display:flex;align-items:center;justify-content:center;gap:10px;font-size:20px;font-weight:500;color:#333}
  .tool i{display:block;width:20px;height:20px;background:#555}

  .footer-band{left:0;top:2248px;width:1200px;height:460px;background:var(--dark)}
  .cta{left:104px;top:2144px;width:992px;height:304px;background:var(--orange);border-radius:12px;text-align:center;color:var(--white)}
  .cta h2{margin-top:54px;font-size:34px;line-height:42px;font-weight:700;text-transform:uppercase;padding:0 70px}
  .cta-actions{margin-top:30px;display:flex;justify-content:center;gap:14px}
  .cta-actions a{height:42px;line-height:40px;padding:0 22px;font-size:14px;font-weight:700;border-radius:4px;text-decoration:none;letter-spacing:.5px}
  .cta-primary{background:var(--dark);color:var(--white);border:1px solid var(--dark)}
  .cta-ghost{border:1.5px solid var(--white);color:var(--white)}

  .site-footer .brand{left:0;width:1200px;text-align:center;top:2500px;font-size:42px}
  .footer-nav{left:0;top:2584px;width:1200px;display:flex;justify-content:center;gap:24px;font-size:16px}
  .footer-nav a{color:var(--white);text-decoration:none}
  .footer-nav a.active{font-weight:700}
  .copyright{left:0;top:2666px;width:1200px;text-align:center;font-size:12px;color:#cfcfcf}
</style>
</head>
<body>
  <div class="abs hero-band"></div>

  <header class="site-header">
    <div class="abs brand">Tarnvale</div>
    <nav class="abs main-nav">
      <a class="active" href="#">Home</a><a href="#">About Us</a><a href="#">Featurees</a><a href="#">Pricinge</a><a href="#">Docse</a><a href="#">Status</a>
    </nav>
    <a class="abs btn btn-signin" href="#">SIGN IN</a>
  </header>

  <section class="hero">
    <h1 class="abs hero-title"><em>Orbinex Enterprise</em> App Management<br>Made Easy</h1>
    <p class="abs hero-sub">Keep your private Orbinex application self-updated without any third-party process.</p>
    <a class="abs btn btn-hero" href="#">SIGN UP FREE</a>
    <div class="abs hero-photo" role="img" aria-label="Photo of a smiling developer in a green jacket using a smartphone in a bright office"></div>
  </section>

  <section class="quick-usage">
    <h2 class="abs section-title" style="top:904px"><em>Quick</em> Usage</h2>
    <div class="abs step" style="left:252px;top:992px">
      <div class="step-num">01</div><div class="step-name">Download</div><div class="step-detail">Bramble,Keelset,JAR</div>
    </div>
    <div class="abs step" style="left:528px;top:992px">
      <div class="step-num">02</div><div class="step-name">Configure</div><div class="step-detail">OrbinexManifest.xml</div>
    </div>
    <div class="abs step" style="left:828px;top:992px">
      <div class="step-num">03</div><div class="step-name">Call</div><div class="step-detail">Tarnvale.start()</div>
    </div>
  </section>

  <section class="strategies">
    <div class="abs strategies-band"></div>
    <h2 class="abs section-title" style="top:1330px"><em>Update</em> Strategies</h2>
    <div class="abs strategy" style="left:104px;top:1432px">
      <div class="strategy-shot" role="img" aria-label="Hand holding a phone showing a status bar update notice" style="background:linear-gradient(160deg,#9a9a92,#5d5a55)"><div class="notice" style="top:96px;height:30px"></div></div>
      <div class="strategy-name">Status Bar</div>
    </div>
    <div class="abs strategy" style="left:356px;top:1432px">
      <div class="strategy-shot" role="img" aria-label="Hand holding a phone showing a friendly update pop-up" style="background:linear-gradient(160deg,#b7b3ad,#6a655f)"><div class="notice" style="top:100px;height:56px"></div></div>
      <div class="strategy-name">Friendly Pop-up</div>
    </div>
    <div class="abs strategy" style="left:608px;top:1432px">
      <div class="strategy-shot" role="img" aria-label="Hand holding a phone showing a blocking update pop-up" style="background:linear-gradient(160deg,#a9a7a3,#5f5b57)"><div class="notice" style="top:100px;height:56px"></div></div>
      <div class="strategy-name">Annoying Pop-up</div>
    </div>
    <div class="abs strategy" style="left:860px;top:1432px">
      <div class="strategy-shot" role="img" aria-label="Hand holding a phone showing an update icon in the status bar" style="background:linear-gradient(160deg,#c3c1bd,#77726c)"></div>
      <div class="strategy-name">Status Bar</div>
    </div>
  </section>

  <section class="tools">
    <h2 class="abs section-title" style="top:1932px;color:var(--orange)">Tools</h2>
    <div class="abs tool" style="left:104px;top:2004px"><i></i>Mirovane</div>
    <div class="abs tool" style="left:302px;top:2004px"><i></i>Cordelix</div>
    <div class="abs tool" style="left:500px;top:2004px"><i></i>Fluxen</div>
    <div class="abs tool" style="left:698px;top:2004px"><i></i>Reactor Kit</div>
    <div class="abs tool" style="left:896px;top:2004px"><i></i>Bramble</div>
  </section>

  <div class="abs footer-band"></div>
  <section class="abs cta">
    <h2>Host your APK, manage and enforce versions, track exceptions and installations, integrate with our API, and much more!</h2>
    <div class="cta-actions">
      <a class="cta-primary" href="#">SIGN UP FREE</a>
      <a class="cta-ghost" href="#">SEE PRICING</a>
      <a class="cta-ghost" href="#">SEE ALL FEATURES</a>
    </div>
  </section>

  <footer class="site-footer">
    <div class="abs brand">Tarnvale</div>
    <nav class="abs footer-nav">
      <a class="active" href="#">Home</a><a href="#">About Us</a><a href="#">Featurees</a><a href="#">Pricinge</a><a href="#">Docse</a><a href="#">Status</a>
    </nav>
    <p class="abs copyright">© Tarnvale Terms and Privacy</p>
  </footer>
</body>
</html>
```